Willowmere Rites Studio creates individual, personalised ceremonies to celebrate weddings, naming days,coming of age, significant age, divorce and final resting rites. Ceremonies and meaningful rituals are created in collaboration with the individual to reflect their hopes and desires, how they will/have embrace/d their lives. The final design should have the logo (purple) on a white/silver background on the right hand side of the card. Name of business and contact details in red on a black background on the left
Updates

Hi All, have only just realised I have paid for a double sided card, yep, a newbie! Sorry to set the cat amongst the pigeons but could we put 'creating...... etc' on the back?

Target Market(s)

Couples marrying, renewing of vows, baby naming days, coming of age, significant age, divorce, funeral ceremonies. The target market predominantly will be couples marrying.

Industry/Entity Type

Business

Contact Information for Business Card

Willowmere Rites Studio, Tamsin Crowther, 0492-718305 willowmereritesstudio1@quillpost.net
"Crafting singular, bespoke occasions honouring journeys"

Font styles to use
Script

Colors
eb1f27
6b449b
f3f0f8

Requirements
Must have
• On initial entry, and now, the logo was not displayed in full - the bottom part was cut off - this needs to be in it's entirety. Colours as previously specified are non-negotiable. Font and placement of characters will be assessed as produced.
Should not have
• Telephone symbol, call us, director,grammatical symbols ( : )

```html
<!DOCTYPE html>
<html lang="en">
<head>
<meta charset="utf-8">
<title>Willowmere Rites Studio – Business Card</title>
<link rel="stylesheet" href="https://fonts.googleapis.com/css2?family=Dancing+Script:wght@500&family=Open+Sans:wght@400;600&display=swap">
<style>
  :root {
    --stage: #e6e4e8;
    --card-black: #050505;
    --brand-red: #eb1f27;
    --brand-purple: #6b449b;
    --silver-light: #f3f0f8;
    --silver-mid: #d9d8dc;
    --silver-dark: #b9b8bd;
    --faint-mark: #1c1c1c;
  }
  * { box-sizing: border-box; margin: 0; padding: 0; }
  html, body {
    width: 1200px;
    height: 784px;
    overflow: hidden;
    background: var(--stage);
    font-family: "Open Sans", Arial, sans-serif;
  }
  .sheet {
    position: relative;
    width: 1200px;
    height: 784px;
  }
  .card {
    position: absolute;
    top: 232px;
    width: 560px;
    height: 320px;
    background: var(--card-black);
    overflow: hidden;
    box-shadow: 0 3px 10px rgba(0,0,0,0.18);
  }
  .card--back { left: 30px; }
  .card--front { left: 610px; }

  /* Back side */
  .back-mark {
    position: absolute;
    left: 0; right: 0;
    top: 28px;
    text-align: center;
    font-family: "Dancing Script", "Brush Script MT", cursive;
    font-size: 44px;
    font-weight: 500;
    line-height: 1.05;
    color: var(--faint-mark);
  }
  .back-tagline {
    position: absolute;
    left: 0; right: 0;
    top: 150px;
    text-align: center;
    font-size: 14px;
    letter-spacing: 1.1px;
    color: var(--brand-red);
  }

  /* Front side */
  .front-panel {
    position: absolute;
    inset: 0;
    width: 560px;
    height: 320px;
  }
  .studio-name {
    position: absolute;
    left: 34px;
    top: 46px;
    width: 220px;
    font-family: "Dancing Script", "Brush Script MT", cursive;
    font-size: 38px;
    font-weight: 500;
    line-height: 1.05;
    color: var(--brand-purple);
  }
  .panel-mark {
    position: absolute;
    right: 38px;
    top: 62px;
    width: 150px;
    text-align: center;
  }
  .panel-mark__dot {
    display: block;
    width: 62px;
    height: 62px;
    margin: 0 auto 12px;
    border-radius: 50%;
    background: var(--brand-purple);
  }
  .panel-mark__name {
    font-family: "Dancing Script", "Brush Script MT", cursive;
    font-size: 26px;
    font-weight: 500;
    line-height: 1.05;
    color: var(--brand-purple);
  }
  .contact {
    position: absolute;
    left: 34px;
    top: 204px;
    color: var(--brand-red);
  }
  .contact__person {
    font-size: 19px;
    font-weight: 600;
    margin-bottom: 14px;
  }
  .contact__line {
    font-size: 14.5px;
    font-weight: 400;
    line-height: 1.4;
  }
</style>
</head>
<body>
  <main class="sheet">
    <section class="card card--back" aria-label="Card back">
      <div class="back-mark">Willowmere<br>Rites Studio</div>
      <p class="back-tagline">"Crafting singular, bespoke occasions honouring journeys"</p>
    </section>

    <section class="card card--front" aria-label="Card front">
      <svg class="front-panel" viewBox="0 0 560 320" aria-hidden="true">
        <defs>
          <linearGradient id="silver" x1="0" y1="0" x2="1" y2="1">
            <stop offset="0" stop-color="var(--silver-dark)"/>
            <stop offset="0.45" stop-color="var(--silver-light)"/>
            <stop offset="1" stop-color="var(--silver-mid)"/>
          </linearGradient>
        </defs>
        <path class="accent-band" d="M262 0 C262 120 300 230 380 320 L560 320 L560 0 Z" fill="var(--brand-red)"/>
        <path class="silver-panel" d="M292 0 C292 120 318 230 392 320 L560 320 L560 0 Z" fill="url(#silver)"/>
      </svg>

      <h1 class="studio-name">Willowmere<br>Rites Studio</h1>

      <div class="panel-mark">
        <span class="panel-mark__dot"></span>
        <span class="panel-mark__name">Willowmere<br>Rites Studio</span>
      </div>

      <div class="contact">
        <p class="contact__person">Tamsin Crowther</p>
        <p class="contact__line">0492-718305</p>
        <p class="contact__line">willowmereritesstudio1@quillpost.net</p>
      </div>
    </section>
  </main>
</body>
</html>
```